The Pixel Tap Business card.

A Simple card with our Logo and contact information. To give to investors and other professionals.

We are a nerd themed bar.
our target market is young professionals age 21+ but the real purpose of this business card is to present to potential investors and other professionals with our contact information. as we are still looking for funding before we start up.

I am partial to green and my partner likes red we are open to iteration.

Target Market(s)

Investors

Industry/Entity Type

Business

Contact Information for Business Card

Martin Hale (225) 730-6192 kent.h4711@mailnest.test Glen Porter (225) 968-5037 glenp318@mailnest.test

Font styles to use
Serif

Requirements
Nice to have
• Keep it simple but not boring.
• Use the Logos but feel free to edit them to match theme/colors.
• Keep the back clean and use one of the Logos.

```html
<!DOCTYPE html>
<html lang="en">
<head>
<meta charset="utf-8">
<title>The Pixel Tap – Business Card</title>
<link rel="stylesheet" href="https://fonts.googleapis.com/css2?family=Source+Sans+3:wght@400;600&display=swap">
<style>
  :root {
    --canvas: #ffffff;
    --card-dark: #000000;
    --card-red: #e01f26;
    --accent: #e3262d;
    --text-light: #ffffff;
  }
  * { margin: 0; padding: 0; box-sizing: border-box; }
  html, body {
    width: 1200px; height: 900px; overflow: hidden;
    background: var(--canvas);
    font-family: "Source Sans 3", "Myriad Pro", Arial, sans-serif;
  }
  .stage { position: relative; width: 1200px; height: 900px; }

  .card { position: absolute; width: 477px; height: 294px; }
  .card-front {
    left: 120px; top: 275px;
    background: var(--card-dark);
    border-radius: 0 48px 0 62px;
  }
  .card-back {
    left: 606px; top: 273px;
    background: var(--card-red);
    border-radius: 48px 0 62px 0;
  }

  .brand-name {
    position: absolute;
    color: var(--text-light);
    font-weight: 600;
    letter-spacing: 1px;
    white-space: nowrap;
    text-transform: uppercase;
  }
  .card-front .brand-name { left: 45px; top: 50px; font-size: 30px; }
  .card-back .brand-name { left: 0; right: 0; top: 124px; text-align: center; font-size: 36px; }

  .contacts {
    position: absolute; right: 29px; top: 136px;
    text-align: right; color: var(--text-light);
  }
  .person + .person { margin-top: 14px; }
  .person-name {
    color: var(--accent); font-weight: 600; font-size: 17px; line-height: 20px;
    margin-bottom: 6px;
  }
  .contact-line {
    font-size: 13px; line-height: 17px;
    display: flex; justify-content: flex-end; align-items: center; gap: 9px;
  }
  .contact-icon { width: 10px; height: 10px; fill: var(--accent); flex: none; }
</style>
</head>
<body>
<div class="stage">

  <section class="card card-front">
    <div class="brand-name">The Pixel Tap</div>

    <div class="contacts">
      <div class="person">
        <div class="person-name">Martin Hale</div>
        <div class="contact-line">(225) 730-6192
          <svg class="contact-icon" viewBox="0 0 10 10"><path d="M2.2 0.5 L3.8 2.6 L2.9 3.7 Q4 5.9 6.3 7.1 L7.4 6.2 L9.5 7.8 L8.4 9.5 Q4.5 9.3 2.2 6.8 Q0.4 4.6 0.5 1.6 Z"/></svg>
        </div>
        <div class="contact-line">kent.h4711@mailnest.test
          <svg class="contact-icon" viewBox="0 0 10 10"><path d="M0.5 2 H9.5 V8 H0.5 Z M1 2.5 L5 5.4 L9 2.5" fill="var(--accent)" stroke="var(--card-dark)" stroke-width="0.8"/></svg>
        </div>
      </div>
      <div class="person">
        <div class="person-name">Glen Porter</div>
        <div class="contact-line">(225) 968-5037
          <svg class="contact-icon" viewBox="0 0 10 10"><path d="M2.2 0.5 L3.8 2.6 L2.9 3.7 Q4 5.9 6.3 7.1 L7.4 6.2 L9.5 7.8 L8.4 9.5 Q4.5 9.3 2.2 6.8 Q0.4 4.6 0.5 1.6 Z"/></svg>
        </div>
        <div class="contact-line">glenp318@mailnest.test
          <svg class="contact-icon" viewBox="0 0 10 10"><path d="M0.5 2 H9.5 V8 H0.5 Z M1 2.5 L5 5.4 L9 2.5" fill="var(--accent)" stroke="var(--card-dark)" stroke-width="0.8"/></svg>
        </div>
      </div>
    </div>
  </section>

  <section class="card card-back">
    <div class="brand-name">The Pixel Tap</div>
  </section>

</div>
</body>
</html>
```